Marlowe Restoration & Remodeling Group LLC

Roofing, windows, gutters services offered.
0% 6 months interest free financing
Quorvin windows
Tillbrook windows
RUV roofing shingles
PEM roofing shingles
Offering 30-50 year warranties.
Accepting all major credit cards, checks
Emergency services available
Updates

Went on vacation/holiday

Target Market(s)

Roofing contractors

Industry/Entity Type

Roofing

Number of Pages Required

3 page

Font styles to use
Sans Serif

Requirements
Must have
• MUST HAVE SEO all necessary codes!!!!!!!!!!
• also I want button for "schedule appointment" so I can receive notification of an appointment, and also need live calendar integrated in that button
Nice to have
• Modern, professional site

```html
<!DOCTYPE html>
<html lang="en">
<head>
<meta charset="utf-8">
<title>Marlowe Restoration &amp; Remodeling Group LLC | Roofing, Windows &amp; Gutters</title>
<meta name="description" content="Marlowe Restoration & Remodeling Group LLC offers roofing, windows and gutters with 0% 6 months interest free financing, 30-50 year warranties and emergency services.">
<meta name="viewport" content="width=1200">
<link rel="stylesheet" href="https://fonts.googleapis.com/css2?family=Cinzel:wght@400;700&family=Lato:wght@400;700&display=swap">
<style>
:root{
  --navy:#1b2a5a;
  --navy-deep:#17244d;
  --teal:#1f8f95;
  --blue:#22579b;
  --ink:#151515;
  --text:#555b66;
  --field:#efefef;
  --line:#d9d9d9;
  --white:#ffffff;
}
*{margin:0;padding:0;box-sizing:border-box}
html,body{width:1200px;height:4060px;overflow:hidden;background:var(--white)}
body{position:relative;font-family:"Lato",sans-serif;color:var(--text)}
.abs{position:absolute}
.serif{font-family:"Cinzel",serif}
.photo{position:absolute}

/* header */
.site-header{position:absolute;left:0;top:0;width:1200px;height:90px;background:var(--white)}
.brand{position:absolute;display:flex;align-items:center;gap:10px;font-family:"Cinzel",serif;font-weight:700;color:var(--navy);line-height:1.15}
.brand-dot{width:30px;height:30px;border-radius:50%;background:var(--teal);flex:none}
.brand-name{font-size:13px}
.main-nav{position:absolute;top:27px;left:522px;display:flex;gap:0}
.main-nav a{display:block;height:36px;line-height:36px;padding:0 11px;font-family:"Cinzel",serif;font-size:13px;color:var(--navy);text-decoration:none;margin-right:14px}
.main-nav a.active{background:var(--navy);color:var(--white)}

/* hero */
.hero{position:absolute;left:0;top:90px;width:1200px;height:676px;overflow:hidden}
.hero-panel{position:absolute;left:0;top:0;width:563px;height:676px;background:linear-gradient(180deg,#1d3f78 0%,#1d6a8c 50%,#1f969a 100%)}
.hero-photo{left:563px;top:0;width:637px;height:676px;background:linear-gradient(160deg,#3c6cae 0%,#8aa8b8 35%,#a88a5e 60%,#4a3a30 80%,#4f8a2e 100%)}
.frame{position:absolute;border:14px solid rgba(255,255,255,.14)}
.hero-title{position:absolute;left:164px;top:182px;font-family:"Cinzel",serif;font-weight:700;font-size:62px;line-height:64px;color:var(--white);letter-spacing:1px}
.btn-dark{position:absolute;left:161px;top:421px;width:262px;height:50px;background:var(--ink);color:var(--white);font-family:"Cinzel",serif;font-size:15px;line-height:50px;text-align:center;text-decoration:none}
.btn-rule{position:absolute;height:2px;background:var(--ink)}
.slides{position:absolute;left:16px;font-family:"Cinzel",serif;color:var(--white)}

/* headings */
.section-title{position:absolute;left:0;width:1200px;text-align:center;font-family:"Cinzel",serif;font-weight:700;color:var(--navy)}
.copy{font-size:11.5px;line-height:20px;color:var(--text)}
.btn-blue{position:absolute;background:var(--blue);color:var(--white);font-family:"Cinzel",serif;font-size:13px;text-align:center;text-decoration:none}
.rule-blue{position:absolute;height:2px;background:var(--blue)}

/* services */
.service-card{position:absolute;width:262px;height:75px;background:var(--white);box-shadow:0 3px 8px rgba(0,0,0,.12);padding:10px 10px 0 10px}
.service-card .kicker{font-family:"Cinzel",serif;font-size:7px;color:var(--teal);font-weight:700}
.service-card h3{font-family:"Cinzel",serif;font-size:19px;color:var(--navy);margin-top:4px;font-weight:700}
.service-card p{font-size:10.5px;color:var(--text);margin-top:2px}

/* financing */
.finance-box{position:absolute;left:0;top:2160px;width:587px;height:391px;background:var(--white);box-shadow:0 0 10px rgba(0,0,0,.1)}
.finance-title{position:absolute;left:613px;top:2162px;font-family:"Cinzel",serif;font-weight:700;font-size:32px;line-height:40px;color:var(--navy)}
.brand-item{position:absolute;font-family:"Cinzel",serif;font-weight:700;font-size:12px;color:var(--ink)}
.brand-item svg{display:block;margin-bottom:16px}

/* testimonial */
.quote-card{position:absolute;left:281px;top:2807px;width:638px;height:186px;background:var(--white);box-shadow:0 0 8px rgba(0,0,0,.1)}
.avatar{position:absolute;left:552px;top:2760px;width:94px;height:94px;border-radius:50%;border:3px solid var(--white);box-shadow:0 0 4px rgba(0,0,0,.3);background:radial-gradient(circle at 50% 40%,#c9b9a8 0%,#6e6a6c 60%,#2a3140 100%)}
.arrow-btn{position:absolute;width:29px;height:29px;border:1px solid var(--navy)}

/* contact */
.field{position:absolute;background:var(--field);border:1px solid var(--line);font-size:11px;color:#777;padding:14px 13px}

/* footer */
.skyline{position:absolute;left:0;top:3498px;width:1200px;height:226px;background:linear-gradient(180deg,#ffffff 0%,#3a3a3a 55%,#0b0b0b 100%)}
.site-footer{position:absolute;left:0;top:3722px;width:1200px;height:338px;background:#0b0b0b}
.foot-head{position:absolute;font-family:"Cinzel",serif;font-size:14px;color:var(--blue);top:49px}
.foot-text{position:absolute;font-size:11.5px;line-height:21px;color:#e8e8e8}
.foot-links{position:absolute;left:388px;top:87px;list-style:none}
.foot-links li{font-size:11.5px;color:#e8e8e8;height:24px;padding-left:16px;position:relative}
.foot-links li::before{content:"";position:absolute;left:0;top:4px;border-left:4px solid var(--blue);border-top:3px solid transparent;border-bottom:3px solid transparent}
.social{position:absolute;width:35px;height:35px;border-radius:50%;border:2px solid #ddd;top:85px}
.card-badge{position:absolute;top:218px;width:35px;height:21px;background:#f2f2f2;border-radius:2px}
</style>
</head>
<body>

<header class="site-header">
  <a class="brand" style="left:158px;top:22px;width:180px" href="#">
    <span class="brand-dot"></span>
    <span class="brand-name">Marlowe Restoration &amp; Remodeling Group LLC</span>
  </a>
  <nav class="main-nav">
    <a class="active" href="#">Home</a>
    <a href="#">About Us</a>
    <a href="#">Services</a>
    <a href="#">Testimonials</a>
    <a href="#">Contact Us</a>
  </nav>
</header>

<section class="hero">
  <div class="hero-panel"></div>
  <div class="photo hero-photo" role="img" aria-label="Photograph of a modern angled roof structure against a cloudy sky"></div>
  <div class="frame" style="left:90px;top:95px;width:563px;height:487px"></div>
  <div class="frame" style="left:131px;top:131px;width:495px;height:404px;border-width:10px;border-color:rgba(255,255,255,.1)"></div>
  <h1 class="hero-title">Marlowe Restoration<br>Remodeling<br>Group LLC</h1>
  <a class="btn-dark" href="#schedule">Schedule an Appointment</a>
  <div class="btn-rule" style="left:359px;top:478px;width:64px"></div>
  <div class="slides" style="top:236px;font-size:15px">01</div>
  <div class="abs" style="left:26px;top:272px;width:1px;height:70px;background:#fff"></div>
  <div class="slides" style="top:355px;font-size:19px">02</div>
  <div class="slides" style="top:390px;font-size:16px">03</div>
  <div class="slides" style="top:418px;font-size:16px">04</div>
</section>

<section>
  <h2 class="section-title" style="top:833px;font-size:37px;line-height:41px">Welcome to Marlowe Restoration<br>Remodeling Group LLC</h2>
  <p class="copy abs" style="left:295px;top:945px;width:610px;text-align:center">Lorem Ipsum is simply dummy text of the printing and typesetting industry. Lorem Ipsum has been the industry's standard dummy text ever since the 1500s, when an unknown printer took a galley of type and scrambled it to make a type specimen book.</p>
  <p class="copy abs" style="left:295px;top:1025px;width:610px;text-align:center">It has survived not only five centuries, but also the leap into electronic typesetting, remaining essentially unchanged.</p>
  <div class="rule-blue" style="left:539px;top:1102px;width:32px"></div>
  <a class="btn-blue" href="#" style="left:539px;top:1112px;width:120px;height:36px;line-height:36px">Read More</a>
  <div class="rule-blue" style="left:629px;top:1156px;width:30px"></div>
</section>

<section>
  <h2 class="abs serif" style="left:162px;top:1224px;font-size:46px;font-weight:700;color:var(--navy)">Our Services</h2>
  <p class="copy abs" style="left:162px;top:1288px;width:330px">Lorem Ipsum is simply dummy text of the printing and typesetting industry. Lorem Ipsum has been the industry's standard dummy text ever since the 1500s.</p>
  <svg class="abs" style="left:162px;top:1362px" width="22" height="20" viewBox="0 0 22 20"><path d="M1 10h18M11 2l8 8-8 8" fill="none" stroke="#22579b" stroke-width="3"/></svg>

  <div class="photo" style="left:672px;top:1222px;width:359px;height:374px;background:linear-gradient(135deg,#1c2a3a 0%,#3c4c5e 45%,#c9d6dd 60%,#c8203f 80%,#e23d5e 100%)" role="img" aria-label="Photograph of a dark and red angled facade"></div>
  <div class="service-card" style="left:672px;top:1558px">
    <div class="kicker">Marlowe Restoration Remodeling Group LLC</div>
    <h3>Roofing &rarr;</h3>
    <p>Lorem Ipsum is simply dummy text of the.</p>
  </div>

  <div class="photo" style="left:229px;top:1460px;width:329px;height:413px;background:linear-gradient(150deg,#3a1f14 0%,#8a4a2a 40%,#5c301c 70%,#2a140c 100%)" role="img" aria-label="Photograph of a timber facade with staggered windows"></div>
  <div class="service-card" style="left:229px;top:1836px">
    <div class="kicker">Marlowe Restoration Remodeling Group LLC</div>
    <h3>Windows &rarr;</h3>
    <p>Lorem Ipsum is simply dummy text of the.</p>
  </div>

  <div class="photo" style="left:672px;top:1703px;width:314px;height:353px;background:linear-gradient(180deg,#3d6a9a 0%,#5f86ad 30%,#e8e8e8 38%,#a8503a 55%,#7a3424 100%)" role="img" aria-label="Photograph of a white gutter on a brick wall"></div>
  <div class="service-card" style="left:672px;top:2017px">
    <div class="kicker">Marlowe Restoration Remodeling Group LLC</div>
    <h3>Gutters &rarr;</h3>
    <p>Lorem Ipsum is simply dummy text of the.</p>
  </div>
</section>

<section>
  <div class="finance-box"></div>
  <div class="abs" style="left:0;top:2176px;width:337px;height:300px;background:var(--navy-deep)"></div>
  <div class="abs" style="left:20px;top:2206px;width:200px;height:250px;border:10px solid rgba(255,255,255,.06)"></div>
  <div class="abs" style="left:41px;top:2230px;width:413px;height:261px;background:var(--teal)"></div>
  <div class="photo" style="left:63px;top:2252px;width:503px;height:280px;background:linear-gradient(180deg,#f2c46a 0%,#f3a94e 45%,#8a4a32 70%,#3a2218 100%)" role="img" aria-label="Photograph of rooftops and a street lamp at sunset"></div>

  <h2 class="finance-title">0% 6 Months Interest<br>Free Financing</h2>

  <div class="brand-item" style="left:624px;top:2294px">
    <svg width="38" height="46" viewBox="0 0 38 46"><rect x="2" y="2" width="34" height="42" fill="none" stroke="#1f8fc4" stroke-width="2.5"/><rect x="8" y="8" width="22" height="28" fill="none" stroke="#1f8fc4" stroke-width="2"/><path d="M19 8v28M8 22h22" stroke="#1f8fc4" stroke-width="2"/></svg>
    Quorvin Windows
  </div>
  <div class="brand-item" style="left:848px;top:2294px">
    <svg width="48" height="46" viewBox="0 0 48 46"><rect x="2" y="4" width="40" height="38" fill="none" stroke="#1f8fc4" stroke-width="2.5"/><path d="M30 4l14-3v44l-14-3z" fill="none" stroke="#1f8fc4" stroke-width="2.5"/></svg>
    Tillbrook Windows
  </div>
  <div class="brand-item" style="left:624px;top:2406px">
    <svg width="46" height="36" viewBox="0 0 46 36"><path d="M2 18L23 3l21 15M8 14v20h30V14" fill="none" stroke="#1f8fc4" stroke-width="2.5"/><rect x="18" y="20" width="10" height="14" fill="none" stroke="#1f8fc4" stroke-width="2"/></svg>
    RUV Roofing Shingles
  </div>
  <div class="brand-item" style="left:848px;top:2406px">
    <svg width="46" height="36" viewBox="0 0 46 36"><path d="M4 34L14 2h8l20 32z M14 2l10 32 M22 20h14" fill="none" stroke="#1f8fc4" stroke-width="2.5"/></svg>
    PEM Roofing Shingles
  </div>
</section>

<section>
  <h2 class="section-title" style="top:2620px;font-size:46px">What Our Client Says</h2>
  <p class="copy abs" style="left:295px;top:2680px;width:610px;text-align:center">Lorem Ipsum is simply dummy text of the printing and typesetting industry. Lorem Ipsum has been the industry's standard dummy text ever since the 1500s.</p>
  <div class="quote-card">
    <svg class="abs" style="left:23px;top:27px" width="38" height="28" viewBox="0 0 38 28"><path d="M2 26V12C2 5 6 2 14 2v6c-4 0-6 2-6 5h6v13zM22 26V12c0-7 4-10 12-10v6c-4 0-6 2-6 5h6v13z" fill="#e2e2e2"/></svg>
    <svg class="abs" style="left:578px;top:126px" width="38" height="28" viewBox="0 0 38 28"><path d="M36 2v14c0 7-4 10-12 10v-6c4 0 6-2 6-5h-6V2zM16 2v14c0 7-4 10-12 10v-6c4 0 6-2 6-5H4V2z" fill="#e2e2e2"/></svg>
    <div class="abs serif" style="left:0;top:56px;width:638px;text-align:center;font-size:14px;font-weight:700;color:var(--navy)">-Client Name</div>
    <p class="copy abs" style="left:58px;top:80px;width:522px;text-align:center">Lorem Ipsum is simply dummy text of the printing and typesetting industry. Lorem Ipsum has been the industry's standard dummy text ever since the 1500s, when an unknown printer took a galley of type and scrambled it to make a type specimen book.</p>
  </div>
  <div class="avatar" role="img" aria-label="Client portrait photograph"></div>
  <div class="arrow-btn" style="left:560px;top:3021px;background:var(--navy)"><svg width="27" height="27" viewBox="0 0 27 27"><path d="M16 8l-6 5.5 6 5.5" fill="none" stroke="#fff" stroke-width="1.6"/></svg></div>
  <div class="arrow-btn" style="left:612px;top:3021px"><svg width="27" height="27" viewBox="0 0 27 27"><path d="M11 8l6 5.5-6 5.5" fill="none" stroke="#1b2a5a" stroke-width="1.6"/></svg></div>
</section>

<section id="schedule">
  <h2 class="section-title" style="top:3115px;font-size:46px">Contact Us</h2>
  <div class="field" style="left:161px;top:3217px;width:281px;height:43px">Name:</div>
  <div class="field" style="left:459px;top:3217px;width:281px;height:43px">Email:</div>
  <div class="field" style="left:757px;top:3217px;width:281px;height:43px">Phone:</div>
  <div class="field" style="left:161px;top:3277px;width:877px;height:88px">Message:</div>
  <div class="rule-blue" style="left:533px;top:3416px;width:30px"></div>
  <a class="btn-blue" href="#" style="left:533px;top:3425px;width:134px;height:35px;line-height:35px">Send Message</a>
  <div class="rule-blue" style="left:635px;top:3468px;width:32px"></div>
</section>

<div class="skyline" role="img" aria-label="City skyline silhouette illustration"></div>

<footer class="site-footer">
  <div class="brand" style="left:161px;top:48px;width:190px;color:#f2f2f2">
    <span class="brand-dot"></span>
    <span class="brand-name">Marlowe Restoration &amp; Remodeling Group LLC</span>
  </div>
  <p class="foot-text" style="left:161px;top:140px;width:200px">Lorem Ipsum is simply dummy text of the printing and typesetting industry. Lorem Ipsum has been the.</p>
  <div class="card-badge" style="left:161px" aria-label="Card accepted"></div>
  <div class="card-badge" style="left:202px"></div>
  <div class="card-badge" style="left:243px"></div>
  <div class="card-badge" style="left:284px"></div>
  <div class="card-badge" style="left:325px"></div>

  <h4 class="foot-head" style="left:388px">View Site Map</h4>
  <ul class="foot-links">
    <li>Home</li><li>About Us</li><li>Services</li><li>Testimonials</li><li>Contact Us</li>
  </ul>

  <h4 class="foot-head" style="left:613px">Contact Info</h4>
  <svg class="abs" style="left:611px;top:86px" width="20" height="20" viewBox="0 0 20 20"><path d="M4 2l4 4-2 3c1 2 3 4 5 5l3-2 4 4-3 3C8 19 1 12 1 5z" fill="#2a78c8"/></svg>
  <div class="foot-text" style="left:643px;top:87px">+1-555-010-2040</div>
  <svg class="abs" style="left:611px;top:128px" width="20" height="14" viewBox="0 0 20 14"><rect x="1" y="1" width="18" height="12" fill="none" stroke="#2a78c8" stroke-width="1.6"/><path d="M1 1l9 7 9-7" fill="none" stroke="#2a78c8" stroke-width="1.6"/></svg>
  <div class="foot-text" style="left:643px;top:124px">support@marloweremodel.com</div>
  <svg class="abs" style="left:612px;top:162px" width="16" height="24" viewBox="0 0 16 24"><path d="M8 1C4 1 1 4 1 8c0 5 7 15 7 15s7-10 7-15c0-4-3-7-7-7z" fill="#2a78c8"/><circle cx="8" cy="8" r="2.6" fill="#0b0b0b"/></svg>
  <div class="foot-text" style="left:643px;top:158px;width:150px;line-height:16px">100- Lorem ipsum is simply dummy text.</div>

  <h4 class="foot-head" style="left:837px">Follow Us On</h4>
  <div class="social" style="left:836px" aria-label="Social profile"></div>
  <div class="social" style="left:890px" aria-label="Social profile"></div>
  <div class="social" style="left:943px" aria-label="Social profile"></div>
  <div class="social" style="left:995px" aria-label="Social profile"></div>
  <div class="abs serif" style="left:852px;top:142px;width:170px;text-align:center;font-size:11px;line-height:20px;color:#8a8a8a">Emergency Services<br>Available</div>
  <div class="abs" style="left:869px;top:186px;width:30px;height:1px;background:#555"></div>
  <a class="btn-blue" href="#schedule" style="left:869px;top:194px;width:136px;height:36px;line-height:36px">Contact Us</a>
  <div class="abs" style="left:975px;top:236px;width:30px;height:1px;background:var(--blue)"></div>

  <div class="abs" style="left:161px;top:273px;width:877px;height:1px;background:#2a2a2a"></div>
  <div class="abs" style="left:0;top:300px;width:1200px;text-align:center;font-size:11px;color:#e8e8e8">Copyright&copy;2019 Marlowe. All Right Reserved. Terms &amp; Conditions.</div>
</footer>

</body>
</html>
```